Website for enterprise software start-up

We need a new Wordpress website. We are an early stage start-up focused on mobile video technology for cellular operators. The audience is strategy, marketing and customer acquisition execs from the operators.

The purpose of the site is to act as a sales brochure and capture leads. A demo app can be downloaded from the current site, want to put that behind a contact form.

Current website is at www.brevlane.tv. Similar number of pages. Looking for a clean design template, with minimal customization. Blog will remain as is.

Want to be able to modify the copy via Wordpress. Reference designs I like: tarnwick.com, tessel4analytics.com

Target Market(s)

Mobile operators and MVNOs in the US and Asia Pacific regions

Industry/Entity Type

Business Software

Coding

Coded - Design and coding required

Number of Pages Required

4 page

Font styles to use
Sans Serif

Colors
f78f20

Requirements
Must have
• Form for downloading sample apps.
• Landing page with image, Product, Blog, About, Contact
• Team page

```html
<!DOCTYPE html>
<html lang="en">
<head>
<meta charset="utf-8">
<title>Brevlane Media — Mobile Engagement</title>
<link href="https://fonts.googleapis.com/css2?family=Montserrat:wght@400;500;600;700;800&display=swap" rel="stylesheet">
<style>
:root{
  --orange:#e8711d;
  --ink:#1d1d1f;
  --text:#5a5a5a;
  --muted:#8d8d8d;
  --line:#e3e3e3;
  --band:#f2f2f2;
  --white:#ffffff;
  --footer:#0d0d0d;
}
*{box-sizing:border-box;margin:0;padding:0}
html,body{width:1200px;height:3982px;overflow:hidden}
body{position:relative;background:var(--white);font-family:'Montserrat',Arial,sans-serif;color:var(--text)}
.abs{position:absolute}
a{color:inherit;text-decoration:none}

/* header */
.site-header{position:absolute;left:0;top:0;width:1200px;height:80px;background:var(--white)}
.brand{position:absolute;left:146px;top:18px;display:flex;align-items:center;gap:10px}
.brand-square{width:38px;height:38px;background:var(--orange)}
.brand-name{font-size:30px;font-weight:700;color:var(--ink);letter-spacing:-0.5px}
.main-nav{position:absolute;left:614px;top:32px;display:flex;gap:30px;font-size:11px;font-weight:500;letter-spacing:1px;color:#6b6b6b;text-transform:uppercase}
.btn-login{position:absolute;left:966px;top:26px;width:88px;height:28px;border-radius:14px;background:var(--orange);color:var(--white);font-size:11px;font-weight:700;letter-spacing:1px;text-align:center;line-height:28px}

/* hero */
.hero{position:absolute;left:0;top:80px;width:1200px;height:544px;overflow:hidden}
.hero-photo{position:absolute;inset:0;background:linear-gradient(90deg,#f4f6f8 0%,#eef2f5 38%,#d9dfe3 62%,#e9a88f 72%,#c7cfd6 86%,#aeb7bf 100%)}
.hero-title{position:absolute;left:146px;top:150px;font-size:46px;line-height:50px;font-weight:800;color:var(--ink);letter-spacing:1px}
.hero-sub{position:absolute;left:146px;top:251px;font-size:33px;font-weight:700;color:var(--orange)}
.hero-text{position:absolute;left:146px;top:298px;width:420px;font-size:13px;line-height:18px;color:#444}
.btn-pill{position:absolute;height:28px;border-radius:14px;font-size:11px;font-weight:700;letter-spacing:1px;text-align:center;line-height:28px;text-transform:uppercase}
.btn-solid{background:var(--orange);color:var(--white)}
.btn-outline{border:1.5px solid var(--orange);color:var(--orange);line-height:25px}

/* feature blocks */
.feature{position:absolute;left:0;width:1200px}
.feature-title{position:absolute;display:flex;align-items:center;gap:12px;font-size:26px;font-weight:600;color:var(--ink)}
.title-square{width:24px;height:24px;background:var(--orange)}
.feature-rule{position:absolute;height:1px;background:var(--orange);opacity:.55}
.feature-lead{position:absolute;font-size:12.5px;line-height:18px;color:var(--muted)}
.feature-list{position:absolute;list-style:none;font-size:12.5px;line-height:18px;color:var(--text)}
.feature-list li{position:relative;padding-left:34px;margin-bottom:7px}
.feature-list li::before{content:"";position:absolute;left:0;top:2px;width:12px;height:12px;border:1.5px solid var(--orange);border-radius:50%;opacity:.7}
.device-shot{position:absolute;border-radius:18px}

/* partners */
.partner-row{position:absolute;left:146px;top:1608px;width:912px;display:flex;justify-content:space-between}
.partner-mark{width:104px;height:44px;background:#d4d4d4;border-radius:6px}
.cert-badge{position:absolute;left:484px;top:1772px;width:222px;height:80px;border-radius:10px;background:#f1f1f1;border:1px solid #e1e1e1}
.cert-badge::before{content:"";position:absolute;left:8px;top:4px;width:72px;height:72px;border-radius:12px;background:#1f5fb0}
.center-note{position:absolute;left:0;width:1200px;text-align:center;font-size:12px;color:var(--muted)}
.center-note span{color:var(--orange)}

/* about */
.about{position:absolute;left:0;top:1933px;width:1200px;height:337px;background:var(--band)}
.center-title{position:absolute;left:0;width:1200px;display:flex;justify-content:center;align-items:center;gap:12px;font-size:21px;font-weight:600;color:var(--ink)}
.center-title .title-square{width:22px;height:22px}
.center-text{position:absolute;left:300px;width:600px;text-align:center;font-size:12.5px;line-height:19px;color:var(--text)}
.center-text strong{display:block;color:#333;font-weight:700;margin-bottom:6px}

/* blog */
.post-card{position:absolute;top:2450px;width:286px;height:224px;border:1px solid var(--line);background:var(--white)}
.post-media{position:absolute;left:0;top:0;width:100%;height:132px;background:linear-gradient(160deg,#3d4a55,#6d6258 55%,#2b2f35)}
.post-title{position:absolute;left:16px;top:12px;right:14px;font-size:17px;line-height:21px;color:var(--white);font-weight:500}
.post-date{position:absolute;left:16px;top:106px;font-size:10px;color:var(--white)}
.post-excerpt{position:absolute;left:16px;top:148px;right:14px;font-size:11.5px;line-height:17px;color:var(--muted)}
.dots{position:absolute;left:582px;top:2720px;display:flex;gap:4px}
.dots i{width:10px;height:10px;border-radius:50%;border:1.5px solid #3f7fd0}
.dots i.on{background:#3f7fd0}

/* sample apps */
.apps-band{position:absolute;left:0;top:2841px;width:1200px;height:340px;background:linear-gradient(90deg,#4c4a47 0%,#6b5f55 22%,#b3a28f 38%,#fff5e6 52%,#f3efe9 70%,#ecebe9 100%)}
.apps-title{position:absolute;left:700px;top:2932px;width:370px;text-align:center;font-size:21px;font-weight:500;color:var(--orange)}
.apps-text{position:absolute;left:740px;top:2974px;width:290px;text-align:center;font-size:12px;line-height:17px;color:#555}
.store-badge{position:absolute;top:3046px;width:106px;height:34px;border-radius:6px;background:#111}

/* contact */
.contact-lead{position:absolute;left:0;top:3275px;width:1200px;text-align:center;font-size:12px;color:var(--muted)}
.contact-lead span{color:var(--orange)}
.field{position:absolute;height:34px;border:1px solid #dedede;background:var(--white);font-size:11.5px;color:#a7a7a7;padding:10px 12px}

/* footer */
.site-footer{position:absolute;left:0;top:3630px;width:1200px;height:352px;background:var(--footer);color:#a9a9a9}
.footer-brand{position:absolute;left:146px;top:84px;display:flex;align-items:center;gap:9px}
.footer-brand .brand-square{width:32px;height:32px}
.footer-brand .brand-name{font-size:26px;color:var(--white)}
.footer-about{position:absolute;left:146px;top:138px;width:180px;font-size:11px;line-height:16px}
.footer-copy{position:absolute;left:146px;top:232px;width:200px;font-size:11px;line-height:16px}
.footer-copy span{color:var(--orange)}
.footer-col{position:absolute;top:82px}
.footer-col h4{font-size:11px;letter-spacing:1.2px;color:var(--white);font-weight:600;margin-bottom:14px;text-transform:uppercase}
.footer-col li{list-style:none;font-size:11px;line-height:20px}
.newsletter-text{font-size:11px;line-height:16px;width:190px}
.newsletter-input{position:relative;margin-top:14px;width:208px;height:26px;background:var(--white);font-size:10.5px;color:#777;padding:7px 8px}
.newsletter-input svg{position:absolute;right:8px;top:6px}
.social li{display:flex;align-items:center;gap:10px;line-height:28px}
.social li i{width:20px;height:20px;border-radius:50%;background:#d9d9d9}
</style>
</head>
<body>

<header class="site-header">
  <div class="brand"><div class="brand-square"></div><div class="brand-name">Brevlane</div></div>
  <nav class="main-nav"><a>Product</a><a>Contact Us</a><a>Blog</a><a>About Us</a></nav>
  <a class="btn-login">LOGIN</a>
</header>

<section class="hero">
  <div class="hero-photo" role="img" aria-label="Photo of a smiling woman in sunglasses and headphones watching video on her phone, city skyline behind"></div>
  <h1 class="hero-title">HIGH<br>QUALITY</h1>
  <div class="hero-sub">Mobile Engagement™</div>
  <p class="hero-text">We engage mobile audiences with the right video content at the perfect moment.</p>
  <a class="btn-pill btn-solid" style="left:146px;top:358px;width:156px">&#9675; Sample Apps</a>
</section>

<section class="feature" style="top:624px;height:438px">
  <div class="feature-title" style="left:146px;top:76px"><span class="title-square"></span>Push Video Notifications</div>
  <div class="feature-rule" style="left:146px;top:118px;width:384px"></div>
  <p class="feature-lead" style="left:146px;top:130px;width:390px">Personalised flawless HD videos, revealed at the perfect moment, as rich media notifications.</p>
  <ul class="feature-list" style="left:146px;top:182px;width:420px">
    <li>Reach your mobile audience with beautiful HD thumbnails and in-notification videos.</li>
    <li>Instant video playback, zero buffering, guaranteed flawless playback - even when offline.</li>
    <li>Content is personalised based on viewer interests and mobile viewing habits.</li>
    <li>Monetise with beautiful HD preroll or interstitial ads.</li>
    <li>Easily added to your existing apps within one hour.</li>
  </ul>
  <div class="device-shot" style="left:637px;top:72px;width:412px;height:340px;background:linear-gradient(135deg,#f2f2f2 0%,#f6c63c 30%,#e94f3d 50%,#3f9bd6 70%,#e8e8e8 100%)" role="img" aria-label="Two smartphones showing a push video notification on the lock screen"></div>
</section>

<section class="feature" style="top:1062px;height:486px;background:var(--band)">
  <div class="device-shot" style="left:106px;top:98px;width:412px;height:388px;border-radius:18px 18px 0 0;background:linear-gradient(135deg,#e6e6e6 0%,#8a6aa8 25%,#2a2a2a 50%,#5b4a3c 75%,#202020 100%)" role="img" aria-label="Two smartphones showing in-app native video with a list of movie trailers"></div>
  <div class="feature-title" style="left:557px;top:104px"><span class="title-square"></span>Native Push Video</div>
  <div class="feature-rule" style="left:557px;top:146px;width:384px"></div>
  <p class="feature-lead" style="left:557px;top:158px;width:390px">Personalised flawless HD videos, discoverable in-app, and playable even when offline.</p>
  <ul class="feature-list" style="left:557px;top:210px;width:420px">
    <li>Guarantee your audience never gets frustrated with a poor quality mobile video streaming experience.</li>
    <li>Instant video playback, zero buffering, HD quality guaranteed - even when offline.</li>
    <li>Content is personalised based on viewer interests and mobile viewing habits.</li>
    <li>Monetise with beautiful HD preroll or interstitial ads.</li>
    <li>Use your existing content management and hosting systems.</li>
  </ul>
</section>

<div class="partner-row">
  <i class="partner-mark"></i><i class="partner-mark"></i><i class="partner-mark"></i><i class="partner-mark"></i><i class="partner-mark"></i><i class="partner-mark"></i><i class="partner-mark"></i>
</div>
<a class="btn-pill btn-outline" style="left:536px;top:1699px;width:128px">Load More</a>
<div class="cert-badge"></div>
<p class="center-note" style="top:1862px"><span>Contact us</span> for details of how to become a Certified Developer Partner</p>

<section class="about">
  <h2 class="center-title" style="top:54px"><span class="title-square"></span>About</h2>
  <div class="center-text" style="top:112px">
    <strong>Cras cursus turpis eu augue placerat, tempor porttitor velit ultricies.</strong>
    Phasellus quis sem at nunc pretium laoreet. Mauris eros urna, consequat quis ultricies a, pulvinar laoreet lacus. Phasellus euismod porttitor tortor, non malesuada odio dapibus. Lorem ipsum dolor sit amet, consectetur adipiscing elit. Egestas eget lacus nec, gravida scelerisque dolor. Suspendisse ac augue ante proin fringilla massa eget accumsan congue.
  </div>
  <a class="btn-pill btn-solid" style="left:525px;top:248px;width:150px">View More</a>
</section>

<section>
  <h2 class="center-title" style="top:2316px"><span class="title-square"></span>Latest Blog Post</h2>
  <p class="center-text" style="top:2368px;font-size:12px;color:var(--muted)">Suspendisse sed pretium tortor. Aliquam congue id libero sit amet lacinia. Nulla facilisi. Nullam ex lectus, mollis nec enim ornare, imperdiet efficitur erat.</p>

  <article class="post-card" style="left:146px">
    <div class="post-media" role="img" aria-label="Blog post photo of a busy city street at night"></div>
    <h3 class="post-title">Duis aute irure dolor in reprehenderit in voluptate velit esse cillum dolore</h3>
    <div class="post-date">September 8, 2014</div>
    <p class="post-excerpt">Lorem ipsum dolor sit amet consectetur adipiscing elit sed do eiusmod tempor incididunt ut labore et dolore magna</p>
  </article>
  <article class="post-card" style="left:457px">
    <div class="post-media" role="img" aria-label="Blog post photo of a brightly lit shop front"></div>
    <h3 class="post-title">Duis aute irure dolor in reprehenderit in voluptate</h3>
    <div class="post-date">August 21, 2014</div>
    <p class="post-excerpt">Sit amet consectetur adipiscing elit sed do eiusmod tempor incididunt ut labore dolore magna aliqua enim adminim</p>
  </article>
  <article class="post-card" style="left:770px">
    <div class="post-media" role="img" aria-label="Blog post photo of a bookshelf in a study"></div>
    <h3 class="post-title">Duis aute irure dolor in reprehenderit in voluptate</h3>
    <div class="post-date">August 19, 2014</div>
    <p class="post-excerpt">Consectetur adipiscing elit sed do eiusmod tempor incididunt ut labore et dolore magna aliqua ad minim</p>
  </article>

  <div class="dots"><i></i><i class="on"></i><i></i></div>
  <a class="btn-pill btn-outline" style="left:525px;top:2755px;width:150px">View More &rarr;</a>
</section>

<section>
  <div class="apps-band" role="img" aria-label="Photo of a man on a plane watching video on his phone by a sunlit window"></div>
  <h2 class="apps-title">Sample Apps</h2>
  <p class="apps-text">Aenean sollicitudin, lorem quis bibendum auctor, nisi elit consequat ipsum, nec sagittis sem nibh id elit. Duis sed odio sit amet nibh vulputate</p>
  <div class="store-badge" style="left:762px"></div>
  <div class="store-badge" style="left:878px"></div>
</section>

<section>
  <h2 class="center-title" style="top:3238px;font-size:19px">Contact Us</h2>
  <p class="contact-lead">Let us know in the form below, email at <span>hello@brevlane.tv</span> or call on <span>1 (555) 014-2290</span></p>
  <div class="field" style="left:345px;top:3326px;width:247px">Your Name</div>
  <div class="field" style="left:608px;top:3326px;width:247px">Your Last Name</div>
  <div class="field" style="left:345px;top:3374px;width:510px">Your Email Address</div>
  <div class="field" style="left:345px;top:3424px;width:510px;height:100px">Your Message</div>
  <a class="btn-pill btn-solid" style="left:475px;top:3538px;width:250px;height:34px;line-height:34px;border-radius:17px">Send Messages</a>
</section>

<footer class="site-footer">
  <div class="footer-brand"><div class="brand-square"></div><div class="brand-name">Brevlane</div></div>
  <p class="footer-about">Ut lacinia turpis quis arcu iaculis accumsan. Aenean condimentum consequat euismod. Ut sodales ullamcorper quam ut tempus.</p>
  <p class="footer-copy">© 2016 <span>Brevlane Media, Inc.</span> All rights reserved. Privacy Policy</p>
  <div class="footer-col" style="left:378px"><h4>Navigation</h4><ul><li>Product</li><li>Contact Us</li><li>Blog</li><li>About Us</li></ul></div>
  <div class="footer-col" style="left:534px"><h4>Help</h4><ul><li>Contact us</li><li>FAQ</li><li>Terms &amp; Conditions</li><li>Privacy Policy</li><li>Feedback</li><li>Sitemap</li></ul></div>
  <div class="footer-col" style="left:690px"><h4>Signup for our newsletter</h4>
    <p class="newsletter-text">Phasellus pellentesque pretium. Nullam tempor tempor massa in.</p>
    <div class="newsletter-input">Enter your email
      <svg width="14" height="14" viewBox="0 0 14 14"><path d="M1 7 13 1 9 13 7 8Z" fill="#111"/></svg>
    </div>
  </div>
  <div class="footer-col social" style="left:922px"><h4>Connect with us</h4><ul><li><i></i>Circlefeed</li><li><i></i>Chirpline</li><li><i></i>Linkwork</li></ul></div>
</footer>

</body>
</html>
```